First Aid Training business needs business card design

We would like a double sided business card designed for a first aid training business - Brindlewood First Aid. We provide first aid training and , WHS (work, health and safety) training.

The attached word document contains the key information we would like on each side of the business card.

Final design needs to be delivered in print ready format, along with the original file.

```html
<!DOCTYPE html>
<html lang="en">
<head>
<meta charset="utf-8">
<title>Brindlewood First Aid – Onsite Training</title>
<link href="https://fonts.googleapis.com/css2?family=EB+Garamond:wght@400;500&display=swap" rel="stylesheet">
<style>
  :root {
    --card-dark: #242323;
    --card-black: #000000;
    --frame-line: #121212;
    --band-orange: #f85314;
    --band-red: #f81d12;
    --band-deep-red: #fb0f10;
    --text-light: #ffffff;
    --panel-light: #f2f2f2;
    --brand-ink: #1a1a1a;
    --brand-dot: #ec1c24;
  }
  html, body {
    margin: 0;
    padding: 0;
    width: 1200px;
    height: 720px;
    overflow: hidden;
    background: #ffffff;
  }
  .card {
    position: relative;
    width: 1200px;
    height: 720px;
    overflow: hidden;
    background: linear-gradient(90deg, var(--card-dark) 0%, #262423 78%, var(--card-black) 100%);
    font-family: "EB Garamond", Garamond, serif;
    color: var(--text-light);
  }
  .inner-frame {
    position: absolute;
    left: 43px;
    top: 44px;
    width: 1114px;
    height: 200px;
    border: 1px solid var(--frame-line);
    border-bottom: none;
  }
  .headline {
    position: absolute;
    left: 0;
    width: 1200px;
    top: 62px;
    margin: 0;
    text-align: center;
    font-weight: 400;
    font-size: 50px;
    letter-spacing: 4px;
    line-height: 1;
  }
  .feature-band {
    position: absolute;
    left: 0;
    top: 152px;
    width: 1200px;
    height: 372px;
  }
  .benefits {
    position: absolute;
    left: 266px;
    top: 225px;
    margin: 0;
    padding: 0;
    list-style: none;
    font-size: 48px;
    line-height: 75px;
  }
  .benefits li {
    position: relative;
    padding-left: 53px;
  }
  .benefits li::before {
    content: "";
    position: absolute;
    left: 2px;
    top: 33px;
    width: 13px;
    height: 13px;
    border-radius: 50%;
    background: var(--text-light);
  }
  .services {
    position: absolute;
    left: 156px;
    top: 556px;
    font-size: 26px;
    line-height: 31px;
    letter-spacing: 0.5px;
  }
  .accent-rule {
    position: absolute;
    left: 60px;
    top: 650px;
    width: 583px;
    height: 7px;
    border-radius: 4px;
    background: linear-gradient(90deg, var(--band-orange), var(--band-red));
  }
  .brand-panel {
    position: absolute;
    left: 696px;
    top: 524px;
    width: 461px;
    height: 144px;
  }
  .brand-dot {
    position: absolute;
    left: 806px;
    top: 560px;
    width: 62px;
    height: 62px;
    border-radius: 50%;
    background: var(--brand-dot);
  }
  .brand-name {
    position: absolute;
    left: 886px;
    top: 562px;
    color: var(--brand-ink);
    font-weight: 500;
    line-height: 1;
  }
  .brand-name .brand-main {
    display: block;
    font-size: 34px;
    letter-spacing: 1px;
  }
  .brand-name .brand-sub {
    display: block;
    margin-top: 4px;
    font-size: 17px;
    letter-spacing: 1.6px;
  }
</style>
</head>
<body>
  <div class="card">
    <div class="inner-frame"></div>
    <h1 class="headline">Onsite Training – We can come to you</h1>

    <svg class="feature-band" viewBox="0 0 1200 372" aria-hidden="true">
      <defs>
        <linearGradient id="capGradient" x1="0" y1="0" x2="1" y2="0">
          <stop offset="0" stop-color="#f85314"/>
          <stop offset="1" stop-color="#f81212"/>
        </linearGradient>
        <linearGradient id="waveGradient" x1="0" y1="0" x2="1" y2="0">
          <stop offset="0" stop-color="#f85314"/>
          <stop offset="1" stop-color="#f81d12"/>
        </linearGradient>
        <linearGradient id="endGradient" x1="0" y1="0" x2="1" y2="0">
          <stop offset="0" stop-color="#f81a12"/>
          <stop offset="1" stop-color="#f85314"/>
        </linearGradient>
      </defs>
      <path d="M171 0 H205 V372 H171 C76 372 0 289 0 186 C0 83 76 0 171 0 Z" fill="url(#capGradient)"/>
      <rect x="950" y="0" width="250" height="372" fill="#fb0f10"/>
      <path d="M990 0 C1085 0 1160 83 1160 186 C1160 289 1085 372 990 372 H950 V0 Z" fill="url(#endGradient)"/>
      <path d="M199 0 C165 75 140 120 140 186 C140 255 165 300 199 372 H960 C995 300 1021 255 1021 186 C1021 120 995 75 960 0 Z" fill="url(#waveGradient)"/>
    </svg>

    <ul class="benefits">
      <li>Time efficient</li>
      <li>Cost effective</li>
      <li>Minimise downtime for your team</li>
    </ul>

    <div class="services">
      <div>First Aid Training</div>
      <div>WHS Training</div>
    </div>
    <div class="accent-rule"></div>

    <svg class="brand-panel" viewBox="0 0 461 144" aria-hidden="true">
      <path d="M67 0 H461 V126 Q461 144 443 144 H14 Q0 144 6 130 Z" fill="#f2f2f2"/>
    </svg>
    <div class="brand-dot"></div>
    <div class="brand-name">
      <span class="brand-main">BRINDLEWOOD</span>
      <span class="brand-sub">FIRST AID TRAINING</span>
    </div>
  </div>
</body>
</html>
```